Halloway Crest Backers Guild business cards

Create a single-sided business card for the Halloway Crest Backers Guild based on the attached logo.
The additional data fields include Name, Title, Email, Phone, and website.
Please use the following as sample data:
Name: Dean Varrow
Title: Co-Founder / Investor
Email: deanvarrow@mailtern.net
Phone: 555-314-2706
Website: www.hcbackersguild.com

Target Market(s)

Start ups, entrepreneurs, venture capitalists

Industry/Entity Type

Investment

Contact Information for Business Card

Professional business card. Technology company.

Font styles to use
Serif
Sans Serif

Requirements
Must have
• Include the HCBG logo (attached)
• Name
• Title
• Email
• Phone
• Website
Should not have
• Cute, cartoony

```html
<!DOCTYPE html>
<html lang="en">
<head>
<meta charset="utf-8">
<title>Halloway Crest Backers Guild – Business Card</title>
<link rel="stylesheet" href="https://fonts.googleapis.com/css2?family=Open+Sans:wght@400;600;700&display=swap">
<style>
  :root {
    --backdrop: #e9e6e3;
    --card-front: #f3f3f3;
    --card-back: #ffffff;
    --brand-green: #1e8c45;
    --ink-dark: #3a3a3a;
    --ink-body: #333333;
    --ink-emboss: #a9a9a9;
    --rule-emboss: #d4d4d4;
  }
  * { margin: 0; padding: 0; box-sizing: border-box; }
  html, body {
    width: 1200px; height: 900px; overflow: hidden;
    background: var(--backdrop);
    font-family: "Open Sans", Arial, sans-serif;
  }
  .card {
    position: absolute;
    box-shadow: 0 6px 18px rgba(0,0,0,0.18);
    overflow: hidden;
  }
  .card--front { left: 238px; top: 62px; width: 555px; height: 342px; background: var(--card-front); }
  .card--back  { left: 457px; top: 518px; width: 560px; height: 342px; background: var(--card-back); }

  .card__band { position: absolute; inset: 0; width: 100%; height: 100%; }

  .brand {
    position: absolute; display: flex; align-items: center;
  }
  .brand--front { left: 36px; top: 36px; }
  .brand__mark {
    width: 16px; height: 16px; margin-right: 14px; background: var(--brand-green);
  }
  .brand__name {
    font-weight: 600; font-size: 22px; line-height: 27px; color: var(--brand-green);
  }
  .brand--back { left: 50%; top: 50%; transform: translate(-50%, -50%); }
  .brand--back .brand__mark { background: var(--ink-emboss); }
  .brand--back .brand__name { color: var(--ink-emboss); font-weight: 400; font-size: 24px; line-height: 29px; }

  .person { position: absolute; left: 35px; top: 168px; }
  .person__name {
    font-family: Arial, "Open Sans", sans-serif;
    font-weight: 700; font-size: 23px; color: var(--brand-green); letter-spacing: 0.3px;
  }
  .person__title {
    margin-top: 3px; font-weight: 600; font-size: 14px; color: var(--ink-body);
  }

  .contact { position: absolute; left: 35px; top: 245px; list-style: none; }
  .contact__item {
    display: flex; align-items: center; height: 22px;
    font-size: 14.5px; color: var(--ink-body);
  }
  .contact__icon { width: 11px; height: 11px; margin-right: 10px; fill: var(--brand-green); }
</style>
</head>
<body>

<section class="card card--front" aria-label="Business card front">
  <svg class="card__band" viewBox="0 0 555 342" preserveAspectRatio="none" aria-hidden="true">
    <polygon points="459,0 555,0 555,342 263,342" fill="var(--brand-green)"/>
    <line x1="454" y1="0" x2="258" y2="342" stroke="var(--brand-green)" stroke-width="1.2"/>
    <circle cx="445" cy="220" r="62" fill="none" stroke="#ffffff" stroke-width="3" opacity="0.85"/>
  </svg>

  <div class="brand brand--front">
    <span class="brand__mark"></span>
    <span class="brand__name">Halloway Crest<br>Backers Guild</span>
  </div>

  <div class="person">
    <h1 class="person__name">Dean Varrow</h1>
    <p class="person__title">Co-Founder / Investor</p>
  </div>

  <ul class="contact">
    <li class="contact__item">
      <svg class="contact__icon" viewBox="0 0 12 12"><path d="M2 1h2.5l1 3-1.5 1a6 6 0 0 0 3 3l1-1.5 3 1V10a1 1 0 0 1-1 1A9 9 0 0 1 1 2a1 1 0 0 1 1-1z"/></svg>
      555-314-2706
    </li>
    <li class="contact__item">
      <svg class="contact__icon" viewBox="0 0 12 12"><path d="M1 2.5h10v7H1z M1 2.5l5 4 5-4" fill="var(--brand-green)" stroke="#fff" stroke-width="0.8"/></svg>
      deanvarrow@mailtern.net
    </li>
    <li class="contact__item">
      <svg class="contact__icon" viewBox="0 0 12 12"><circle cx="6" cy="6" r="5.5"/><path d="M0.5 6h11M6 0.5c-2.5 3-2.5 8 0 11M6 0.5c2.5 3 2.5 8 0 11" stroke="#fff" stroke-width="0.8" fill="none"/></svg>
      www.hcbackersguild.com
    </li>
  </ul>
</section>

<section class="card card--back" aria-label="Business card back">
  <div class="brand brand--back">
    <span class="brand__mark"></span>
    <span class="brand__name">Halloway Crest<br>Backers Guild</span>
  </div>
</section>

</body>
</html>
```